INTERNATIONAL COMPANY IN MARITIME AIR TRANSPORT AND LOGISTICS

We need a power point model with the attached logo, we organize the transport of goods around the world by plane and boat. We also organize logistics. We would like a creation in the colors of our logo or in agreement with this one. The final design must convey the openness to international, men at the heart of our service and the strength of our company.

Target Market(s)

LUX - Aeronautics - RETAIL

Industry/Entity Type

Retail

Font styles to use
Serif

Colors

Requirements
Must have
• We need a power point model with the attached logo, we organize the transport of goods around the world by plane and boat. We also organize logistics. We would like a creation in the colors of our logo or in agreement with this one. The final design must convey the openness to international, men at the heart of our service and the strength of our company.
Nice to have
Should not have
• FREE

```html
<!DOCTYPE html>
<html lang="en">
<head>
<meta charset="utf-8">
<title>Overseas by Maravel – Slide Template</title>
<link href="https://fonts.googleapis.com/css2?family=Arimo:wght@400;700&family=Domine:wght@700&display=swap" rel="stylesheet">
<style>
  :root {
    --teal-deep: #1a6a8c;
    --teal-mid: #3f8fb0;
    --teal-soft: #6fa9c4;
    --sky: #5bbde4;
    --sky-text: #2a9fd0;
    --ink: #2b2b2b;
    --frame: #c9c9c9;
    --paper: #ffffff;
    --mist: #d9eaf3;
  }
  * { box-sizing: border-box; margin: 0; padding: 0; }
  html, body { width: 1200px; height: 1200px; overflow: hidden; background: var(--paper); }
  .canvas { position: relative; width: 1200px; height: 1200px; }

  .slide { position: absolute; overflow: hidden; background: var(--paper); }
  .slide--framed { border: 1px solid var(--frame); }

  .brand {
    position: absolute; display: flex; align-items: center; gap: 4px;
    font-family: "Arimo", sans-serif; font-weight: 400; font-size: 10px;
    letter-spacing: 1px; color: var(--teal-deep);
  }
  .brand__square { width: 7px; height: 7px; background: var(--sky); }
  .accent-rule { position: absolute; height: 5px; background: var(--sky); }

  /* Cover */
  .cover { left: 335px; top: 105px; width: 530px; height: 298px; background: var(--teal-deep); }
  .cover__map { position: absolute; inset: 0;
    background:
      radial-gradient(ellipse 11% 22% at 44% 62%, rgba(130,185,212,.38), rgba(26,106,140,0) 100%),
      radial-gradient(ellipse 16% 14% at 40% 38%, rgba(130,185,212,.32), rgba(26,106,140,0) 100%),
      radial-gradient(ellipse 22% 16% at 64% 36%, rgba(130,185,212,.32), rgba(26,106,140,0) 100%),
      radial-gradient(ellipse 9% 8% at 85% 78%, rgba(130,185,212,.36), rgba(26,106,140,0) 100%),
      radial-gradient(ellipse 8% 18% at 20% 70%, rgba(130,185,212,.22), rgba(26,106,140,0) 100%),
      radial-gradient(ellipse 14% 12% at 18% 28%, rgba(130,185,212,.22), rgba(26,106,140,0) 100%); }
  .cover__strip { position: absolute; left: 0; top: 48px; width: 530px; height: 63px; display: flex;
    box-shadow: 0 2px 4px rgba(0,0,0,.25); }
  .cover__tile { height: 100%; border-right: 1px solid rgba(255,255,255,.55); }
  .cover__tile:last-child { border-right: 0; }
  .t1 { width: 72px; background: linear-gradient(180deg, #bcdcea, #7fb4cd 55%, #4e8fae); }
  .t2 { width: 73px; background: linear-gradient(200deg, #d4e8f1, #8fbfd5 50%, #3f82a2); }
  .t3 { width: 79px; background: linear-gradient(180deg, #a9d0e3, #5f9fbd 60%, #2f7396); }
  .t4 { width: 69px; background: linear-gradient(180deg, #cfe5ef, #96c3d8 50%, #5d98b5); }
  .t5 { width: 79px; background: linear-gradient(160deg, #b8d9e8, #8bbdd4 55%, #6aa4c0); }
  .t6 { width: 81px; background: linear-gradient(180deg, #c6e0ec, #7bb0ca 60%, #437f9e); }
  .t7 { width: 77px; background: linear-gradient(180deg, #e2eff5, #a9cfe1 55%, #6d9fba); }
  .cover__title { position: absolute; left: 47px; top: 138px; color: var(--paper);
    font-family: "Arimo", sans-serif; text-shadow: 1px 1px 2px rgba(0,0,0,.25); }
  .cover__line { font-size: 25px; line-height: 29px; font-weight: 400; }
  .cover__name { font-size: 42px; line-height: 50px; font-weight: 700; letter-spacing: 3px; }
  .cover .accent-rule { left: 0; top: 270px; width: 423px; }
  .cover__badge { position: absolute; left: 429px; top: 257px; width: 68px; height: 29px; background: var(--paper); }
  .cover__badge .brand { left: 5px; top: 9px; font-size: 9px; }

  /* Contents */
  .contents { left: 337px; top: 433px; width: 526px; height: 296px; }
  .contents__banner { position: absolute; left: 0; top: 0; width: 526px; height: 135px;
    background:
      radial-gradient(ellipse 12% 22% at 14% 30%, rgba(40,110,150,.45), rgba(40,110,150,0) 100%),
      radial-gradient(ellipse 20% 18% at 50% 22%, rgba(30,95,130,.55), rgba(30,95,130,0) 100%),
      radial-gradient(ellipse 10% 12% at 66% 55%, rgba(255,255,255,.55), rgba(255,255,255,0) 100%),
      radial-gradient(ellipse 26% 30% at 82% 50%, rgba(230,242,248,.55), rgba(230,242,248,0) 100%),
      linear-gradient(90deg, #6aa5c2 0%, #9cc8dc 35%, #8fbfd5 60%, #b6d7e6 80%, #88b9d0 100%); }
  .contents__fade { position: absolute; left: 0; top: 95px; width: 526px; height: 45px;
    background: linear-gradient(180deg, rgba(255,255,255,0), var(--paper)); }
  .contents__heading { position: absolute; left: 0; width: 526px; top: 66px; text-align: center;
    font-family: "Arimo", sans-serif; font-size: 28px; font-weight: 400; color: #000; padding-left: 4px;
    text-shadow: 0 0 4px rgba(255,255,255,.9); }
  .agenda { position: absolute; list-style: none; font-family: "Domine", serif; font-weight: 700;
    font-size: 12.5px; letter-spacing: .4px; color: var(--ink); }
  .agenda li { position: absolute; white-space: nowrap; padding-left: 27px; }
  .agenda li::before { content: ""; position: absolute; left: 2px; top: 3px; width: 12px; height: 12px;
    background: var(--sky); transform: rotate(45deg); }
  .contents .accent-rule { left: 0; top: 271px; width: 438px; }
  .contents .brand { left: 446px; top: 268px; }

  /* About */
  .about { left: 337px; top: 759px; width: 526px; height: 296px; }
  .about__photo { position: absolute; left: 51px; top: 53px; width: 110px; height: 180px;
    background: linear-gradient(160deg, #e3eef5, #9fb6c8 55%, #2f3b4e);
    box-shadow: 3px 3px 6px rgba(0,0,0,.3); }
  .about__heading { position: absolute; left: 210px; top: 58px; font-family: "Domine", serif;
    font-weight: 700; font-size: 18px; letter-spacing: .5px; color: var(--sky-text); text-decoration: underline; }
  .facts { position: absolute; left: 210px; top: 106px; font-family: "Domine", serif; font-weight: 700;
    font-size: 12.5px; letter-spacing: .4px; color: var(--ink); }
  .facts p { height: 31px; white-space: nowrap; }
  .facts .label { display: inline-block; width: 117px; }
  .about .accent-rule { left: 3px; top: 268px; width: 432px; }
  .about .brand { left: 443px; top: 265px; }
</style>
</head>
<body>
<div class="canvas">

  <section class="slide cover">
    <div class="cover__map" role="img" aria-label="Faint world map backdrop"></div>
    <div class="cover__strip" role="img" aria-label="Strip of transport photos: trucks, port, ship, truck, plane, harbour, lorry">
      <div class="cover__tile t1"></div>
      <div class="cover__tile t2"></div>
      <div class="cover__tile t3"></div>
      <div class="cover__tile t4"></div>
      <div class="cover__tile t5"></div>
      <div class="cover__tile t6"></div>
      <div class="cover__tile t7"></div>
    </div>
    <div class="cover__title">
      <p class="cover__line">Overseas</p>
      <p class="cover__line">by</p>
      <p class="cover__name">Maravel</p>
    </div>
    <div class="accent-rule"></div>
    <div class="cover__badge"><span class="brand"><span class="brand__square"></span>MARAVEL</span></div>
  </section>

  <section class="slide slide--framed contents">
    <div class="contents__banner" role="img" aria-label="Collage of plane, world map, containers and truck in blue tones"></div>
    <div class="contents__fade"></div>
    <h1 class="contents__heading">Sommaire</h1>
    <ul class="agenda" style="left:50px; top:148px;">
      <li style="top:0;">Our company</li>
      <li style="top:39px;">Our offices in France</li>
      <li style="top:74px;">Our network</li>
      <li style="left:228px; top:0;">Our strenghts</li>
      <li style="left:228px; top:39px;">Our tools for supply-chain</li>
    </ul>
    <div class="accent-rule"></div>
    <span class="brand"><span class="brand__square"></span>MARAVEL</span>
  </section>

  <section class="slide slide--framed about">
    <div class="about__photo" role="img" aria-label="Photo of two colleagues working at a laptop"></div>
    <h2 class="about__heading">About us</h2>
    <div class="facts">
      <p><span class="label">Created in</span>: 1991</p>
      <p><span class="label">Turnover</span>: 65 Millions €uros</p>
      <p>100 Employees in France</p>
      <p>300 Employees in Maravel group</p>
    </div>
    <div class="accent-rule"></div>
    <span class="brand"><span class="brand__square"></span>MARAVEL</span>
  </section>

</div>
</body>
</html>
```